Volora Laundry and Dry Cleaning Poster

We need a Poster and Window Sticker for our Laundry and Dry cleaning shop (VOLORA LAUNDRY AND DRY CLEANING).
info we like on the design. Logo is included
Company Name: Volora Laundry and Dry Cleaning
Slogan: It Comes Back Clean
Location: Kwentu-Dasor, Accra
Working Hours: Mon-Sat 8am to 5pm
Tel: +233 30 781 6242
email:info@voloralaundry.example
website: www.voloralaundry.example
fb: fb.com/voloralaundry

Target Market(s)

Laundry Shop

Colors
33a6d7
9bcb3b

```html
<!DOCTYPE html>
<html lang="en">
<head>
<meta charset="utf-8">
<title>Volora Laundry and Dry Cleaning Poster</title>
<link rel="stylesheet" href="https://fonts.googleapis.com/css2?family=Open+Sans:wght@600;700&family=Fira+Sans+Condensed:ital,wght@1,600&display=swap">
<style>
  :root {
    --brand-blue: #1e8bcd;
    --bar-blue: #1f8acb;
    --brand-green: #9bcb3b;
    --photo-dark: #2f2f2f;
    --photo-mid: #4a4a4a;
    --paper: #ffffff;
  }
  html, body {
    margin: 0;
    padding: 0;
    overflow: hidden;
    background: var(--paper);
  }
  .poster {
    position: relative;
    width: 1019px;
    height: 1200px;
    overflow: hidden;
    background: var(--paper);
    font-family: "Open Sans", sans-serif;
  }
  .hero-shapes {
    position: absolute;
    inset: 0;
    width: 1019px;
    height: 1200px;
  }
  .brand-name {
    position: absolute;
    left: 512px;
    top: 488px;
    display: flex;
    align-items: center;
    gap: 18px;
    color: var(--brand-blue);
    font-weight: 700;
  }
  .brand-dot {
    width: 120px;
    height: 120px;
    border-radius: 50%;
    background: var(--brand-blue);
    flex: none;
  }
  .brand-words { line-height: 1; }
  .brand-title {
    display: block;
    font-size: 92px;
    letter-spacing: -1px;
  }
  .brand-sub {
    display: block;
    font-size: 17px;
    margin-top: 10px;
    letter-spacing: 0.2px;
  }
  .hours {
    position: absolute;
    left: 0;
    top: 692px;
    width: 1019px;
    height: 88px;
  }
  .hours-text {
    position: absolute;
    right: 42px;
    top: 0;
    line-height: 88px;
    color: var(--paper);
    font-weight: 700;
    font-size: 31px;
    letter-spacing: 3px;
    word-spacing: 6px;
  }
  .contacts {
    position: absolute;
    left: 54px;
    top: 838px;
    margin: 0;
    padding: 0;
    list-style: none;
  }
  .contact {
    display: flex;
    align-items: center;
    height: 64px;
    color: var(--brand-blue);
    font-size: 30px;
    font-weight: 600;
    letter-spacing: 3px;
  }
  .contact svg {
    width: 48px;
    height: 48px;
    margin-right: 20px;
    flex: none;
  }
  .slogan-bar {
    position: absolute;
    left: 0;
    bottom: 0;
    width: 1019px;
    height: 69px;
    background: var(--bar-blue);
    color: var(--paper);
    text-align: center;
    font-family: "Fira Sans Condensed", sans-serif;
    font-style: italic;
    font-weight: 600;
    font-size: 44px;
    line-height: 69px;
    letter-spacing: 2px;
  }
</style>
</head>
<body>
<div class="poster">
  <svg class="hero-shapes" viewBox="0 0 1019 1200" aria-hidden="false">
    <defs>
      <linearGradient id="photoTone" x1="0" y1="0" x2="1" y2="1">
        <stop offset="0" stop-color="#3a3a3a"/>
        <stop offset="0.5" stop-color="#555555"/>
        <stop offset="1" stop-color="#2a2a2a"/>
      </linearGradient>
    </defs>
    <polygon class="hero-stripe" points="0,770 1019,186 1019,212 0,792" fill="var(--brand-green)"/>
    <polygon class="hero-photo" role="img" aria-label="Photo of an open front-loading washing machine with grey towels inside"
             points="0,0 1019,0 1019,196 0,780" fill="url(#photoTone)"/>
  </svg>

  <div class="brand-name">
    <span class="brand-dot"></span>
    <span class="brand-words">
      <span class="brand-title">volora</span>
      <span class="brand-sub">LAUNDRY AND DRY CLEANING</span>
    </span>
  </div>

  <div class="hours">
    <svg width="1019" height="88" viewBox="0 0 1019 88" aria-hidden="true">
      <polygon points="516,0 1019,0 1019,88 430,88" fill="var(--brand-green)"/>
    </svg>
    <span class="hours-text">MON-SAT :&nbsp; 8AM - 5PM</span>
  </div>

  <ul class="contacts">
    <li class="contact">
      <svg viewBox="0 0 48 48" aria-hidden="true">
        <path d="M24 2C14 2 6 10 6 20c0 12 18 27 18 27s18-15 18-27C42 10 34 2 24 2z" fill="var(--brand-blue)"/>
        <circle cx="24" cy="19" r="7" fill="#fff"/>
      </svg>
      Kwentu-Dasor, Accra
    </li>
    <li class="contact">
      <svg viewBox="0 0 48 48" aria-hidden="true">
        <rect x="5" y="4" width="38" height="40" rx="5" fill="var(--brand-blue)"/>
        <path d="M19 12c-2 0-4 2-4 5 0 8 7 18 14 19 3 0 5-2 5-4l-5-4-3 2c-3-2-5-6-6-9l3-2-2-7z" fill="#fff"/>
      </svg>
      +233 30 781 6242
    </li>
    <li class="contact">
      <svg viewBox="0 0 48 48" aria-hidden="true">
        <rect x="4" y="9" width="40" height="30" fill="var(--brand-blue)"/>
        <path d="M6 11l18 16 18-16M6 37l14-13M42 37L28 24" stroke="#fff" stroke-width="2.5" fill="none"/>
      </svg>
      info@voloralaundry.example
    </li>
    <li class="contact">
      <svg viewBox="0 0 48 48" aria-hidden="true">
        <g fill="none" stroke="var(--brand-blue)" stroke-width="2.5">
          <circle cx="24" cy="24" r="20"/>
          <ellipse cx="24" cy="24" rx="9" ry="20"/>
          <path d="M4 24h40M24 4v40M8 13h32M8 35h32"/>
        </g>
      </svg>
      www.voloralaundry.example
    </li>
  </ul>

  <div class="slogan-bar">It Comes Back Clean</div>
</div>
</body>
</html>
```